Website Refresh Needed - Large Couples Therapy Group

We are a large couples counselling group in Australia, and we have some key pages of our website that need refreshing, as it's a few years old now.
Similar colour palette as currently, and the same colours as the logo. No new logo required.
Total of 7 new (updated) page templates designs are needed:
1. HOME: https://www.thewillowlane.com.au/
2: CONTACT US: https://www.thewillowlane.com.au/contact/
3: RC CITY PAGE: https://www.thewillowlane.com.au/city/sydney/
4: ST CITY PAGE: https://www.thewillowlane.com.au/our-counselling/sex-therapy/sex-therapy-sydney/
5: ALL BLOGS: https://www.thewillowlane.com.au/blog/
6: BLOG: https://www.thewillowlane.com.au/sexual-desires-in-men-and-women-what-are-the-real-differences/
7: MAIN STANDARD PAGE: https://www.thewillowlane.com.au/our-counselling/couples-relationship-counselling/

Target Market(s)

couples who are going through a crisis in their relationship or marriage.

Number of Pages Required

5+ page

Colors
86cfc6
b8a6cd
cfdfed

Requirements
Must have
• Calm, reassuring colours. People are stressed and need to know we can help.
Should not have
• No bright oranges or yellows.

```html
<!DOCTYPE html>
<html lang="en">
<head>
<meta charset="utf-8">
<title>The Willow Lane – Relationship &amp; Marriage Counselling</title>
<link rel="stylesheet" href="https://fonts.googleapis.com/css2?family=Quicksand:wght@400;500;600&family=Montserrat:wght@400;500;600;700&display=swap">
<style>
:root{
  --teal:#1d8591;
  --teal-dark:#17707b;
  --teal-deep:#0f5f69;
  --mint:#86cfc6;
  --lilac:#b8a6cd;
  --pale:#cfdfed;
  --red:#e3222b;
  --ink:#2d3a40;
  --text:#5f6b70;
  --line:#dde6ea;
  --white:#fff;
}
*{box-sizing:border-box;margin:0;padding:0}
html,body{width:1200px;height:5249px;overflow:hidden}
body{font-family:'Montserrat',sans-serif;color:var(--text);background:#fff;position:relative;font-size:11px;line-height:1.6}
.abs{position:absolute}
.ph{position:absolute}
h2,h3{font-family:'Quicksand',sans-serif;font-weight:500;color:var(--ink)}
.eyebrow{font-family:'Quicksand',sans-serif;color:var(--teal);font-size:15px;letter-spacing:1px;text-transform:uppercase;font-weight:500}
.section-title{font-family:'Quicksand',sans-serif;font-size:30px;letter-spacing:1px;text-transform:uppercase;color:var(--ink);font-weight:500;line-height:1.25}
.btn{display:inline-block;background:var(--teal);color:#fff;font-size:10px;font-weight:700;letter-spacing:.5px;text-transform:uppercase;padding:10px 36px;text-decoration:none}
.btn-red{background:var(--red)}
p{margin-bottom:12px}

/* header */
.topbar{position:absolute;top:0;left:0;width:1200px;height:76px;background:#fff}
.toplinks{position:absolute;left:120px;top:30px;font-size:11px;color:var(--text)}
.logo{position:absolute;left:488px;top:14px;display:flex;align-items:center;gap:10px}
.logo .dot{width:40px;height:40px;border-radius:50%;background:var(--teal)}
.logo .name{font-family:'Quicksand',sans-serif;font-size:26px;color:var(--teal);font-weight:500;line-height:1}
.logo small{display:block;font-size:9px;color:var(--teal);font-weight:500}
.head-btn{position:absolute;top:21px;height:34px;font-size:10px;font-weight:700;text-transform:uppercase;display:flex;align-items:center;justify-content:center;gap:8px}
.head-btn.appoint{left:738px;width:184px;background:var(--teal);color:#fff}
.head-btn.phone{left:934px;width:142px;border:1.5px solid var(--teal);color:var(--teal);font-size:11px}
.nav{position:absolute;top:76px;left:0;width:1200px;height:34px;background:var(--teal);display:flex;justify-content:center}
.nav a{color:#fff;font-size:9.5px;font-weight:600;text-transform:uppercase;text-decoration:none;padding:0 14px;line-height:34px}
.nav a.active{background:var(--mint)}

/* hero */
.hero{position:absolute;top:110px;left:0;width:1200px;height:540px;background:linear-gradient(100deg,#e7ebec 0%,#dcdcd8 35%,#cfc7bf 60%,#b6aaa3 100%)}
.hero h1{position:absolute;left:120px;top:68px;font-family:'Quicksand',sans-serif;font-weight:500;font-size:42px;line-height:1.25;color:var(--teal)}
.search{position:absolute;left:122px;top:192px;width:432px;height:190px;background:rgba(29,133,145,.88);padding:18px 44px}
.search h3{color:#fff;text-align:center;font-size:19px;font-weight:400;margin-bottom:14px}
.field{background:#fff;height:32px;font-size:10px;color:#888;padding:0 12px;display:flex;align-items:center;justify-content:space-between}
.row{display:flex;gap:8px;align-items:center;margin-top:10px}
.row .or{color:#fff;font-size:11px}
.search .btn{position:absolute;right:68px;bottom:16px;padding:8px 22px;background:var(--red)}

/* about */
.about-text{position:absolute;left:122px;top:742px;width:420px}
.about-text p{font-size:10.5px}
.about-img{left:590px;top:713px;width:488px;height:374px;background:linear-gradient(135deg,#c9c6c0,#8f8a84 50%,#d8d6d2)}

/* specialise */
.water{background:linear-gradient(180deg,#fff 0%,#e4f1f3 15%,#bfe0e3 45%,#9fd3d6 75%,#fff 100%)}
.spec-band{top:1090px;left:0;width:1200px;height:500px}
.spec-card{position:absolute;left:122px;top:1166px;width:956px;height:350px;background:#fff;box-shadow:0 8px 24px rgba(0,0,0,.08)}
.spec-img{position:absolute;left:0;top:0;width:326px;height:350px;background:linear-gradient(135deg,#e4dcd6,#b8aba3)}
.spec-img .btn{position:absolute;left:62px;bottom:36px;padding:8px 24px}
.spec-body{position:absolute;left:356px;top:30px;width:570px}
.spec-body p{font-size:10.5px}

/* areas */
.center{text-align:center;width:1200px;position:absolute;left:0}
.areas-card{position:absolute;top:1730px;width:306px;height:316px;background:#fff;box-shadow:0 4px 16px rgba(0,0,0,.08);text-align:center}
.areas-card .ph{left:0;top:0;width:306px;height:182px}
.areas-card .badge{position:absolute;left:133px;top:162px;width:40px;height:40px;border-radius:50%;background:#fff;border:2px solid var(--mint)}
.areas-card h4{margin-top:208px;font-size:11px;font-weight:700;color:var(--ink);text-transform:uppercase}
.areas-card .q{font-size:12px;color:var(--ink);margin:8px 0}
.areas-card .d{font-size:10px;padding:0 30px;line-height:1.5}
.arrow{position:absolute;top:1880px;color:var(--teal);font-size:22px}

/* therapists */
.ther{top:2124px;left:0;width:1200px;height:456px;background:linear-gradient(90deg,#127582,#1f8d98 60%,#137683)}
.ther-img{left:120px;top:2145px;width:340px;height:420px;border-radius:48% 48% 50% 50%;background:radial-gradient(circle at 45% 45%,#cfdfed,#86cfc6 55%,#b8a6cd)}
.ther-text{position:absolute;left:478px;top:2178px;color:#fff}
.ther-text .eyebrow{color:#cdeaea}
.ther-text h2{color:#fff;font-size:31px;text-transform:uppercase;font-weight:400;letter-spacing:1px;line-height:1.3}
.ther-text .lead{font-family:'Quicksand',sans-serif;font-size:19px;line-height:1.2;margin-top:2px}
.ther-list{position:absolute;top:2310px;color:#e5f3f3;font-size:13px;line-height:31px;list-style:none}
.ther-list li{display:flex;align-items:center;gap:8px}

/* approach */
.appr-text{position:absolute;left:122px;top:2638px;width:500px}
.appr-text p{font-size:10px;line-height:1.5;margin-bottom:10px}
.appr-img{left:662px;top:2644px;width:416px;height:326px;background:linear-gradient(160deg,#e9ece9,#a7aea9 60%,#5d625e)}
.loc-band{top:3010px;left:0;width:1200px;height:350px;background:linear-gradient(180deg,#fff 0%,#fff 25%,#dbe9ea 55%,#7fa5ab 85%,#fff 100%)}
.loc{position:absolute;left:122px;top:3022px;width:490px}
.loc-grid{display:grid;grid-template-columns:repeat(3,auto);gap:2px 22px;font-size:9.5px;justify-content:start}
.loc-grid b{color:var(--teal)}
.comm{position:absolute;left:648px;top:3022px;width:440px}
.sub-title{font-size:24px;white-space:nowrap;margin-bottom:18px}

/* value boxes */
.vbox{position:absolute;top:3460px;width:306px;height:234px;background:#e1edf5;text-align:center;padding-top:60px}
.vbox .icon{position:absolute;top:-44px;left:113px;width:80px;height:80px;border-radius:50%;background:#e1edf5;border:2px solid #c2d7e3}
.vbox h4{font-family:'Quicksand',sans-serif;font-size:18px;color:var(--teal);font-weight:500;letter-spacing:1px}
.vbox p{font-size:11px;padding:0 40px;margin:16px 0}
.vbox .btn{padding:10px 38px}
.quote{position:absolute;left:772px;top:3418px;width:306px;height:276px;background:linear-gradient(135deg,#86cfc6,#b8a6cd);padding:10px}
.quote div{border:1px solid rgba(255,255,255,.8);height:100%;padding:22px 26px;color:#fff;font-family:'Quicksand',sans-serif;font-size:14px;line-height:1.3;letter-spacing:.5px}
.quote .big{font-size:28px}
.quote .marks{font-size:34px;line-height:.6}

/* tiles */
.tiles-band{top:3740px;left:0;width:1200px;height:340px;background:linear-gradient(180deg,#fff,#dbe8ec 40%,#c7d7dd 60%,#fff)}
.tile{position:absolute;top:3762px;width:306px;height:228px}
.tile .cap{position:absolute;left:0;bottom:0;width:100%;height:42px;background:rgba(29,133,145,.92);color:#fff;font-size:13.5px;text-align:center;line-height:42px}

/* news */
.news-band{top:4080px;left:0;width:1200px;height:860px;background:linear-gradient(180deg,#fff 0%,#fff 70%,#dfe8ec 88%,#b8c9d0 100%)}
.post{position:absolute;width:219px;background:#fff;border:1px solid var(--line)}
.post .ph{position:relative;display:block;width:100%}
.post .txt{padding:12px 18px;font-size:9.5px;line-height:1.35;color:var(--text)}
.post .date{font-size:8px;color:var(--ink);margin-top:6px}
.post .more{color:var(--teal);text-decoration:underline;font-size:9px;display:block;margin-top:4px}

/* footer */
.footer{top:4940px;left:0;width:1200px;height:309px;background:var(--teal);color:#fff}
.footer h5{font-size:10px;font-weight:700;text-transform:uppercase;margin-bottom:20px}
.footer ul{list-style:none;font-size:10px;line-height:21px}
.social{display:flex;gap:8px;margin-top:14px}
.social span{width:24px;height:24px;border-radius:50%;border:1.5px solid #fff}
.contact-item{position:absolute;display:flex;align-items:center;gap:10px;font-size:10px}
.contact-item .ic{width:24px;height:24px;border-radius:50%;background:#fff;display:flex;align-items:center;justify-content:center}
.copy{position:absolute;left:120px;top:264px;width:960px;border-top:1px solid rgba(255,255,255,.3);text-align:center;font-size:8px;padding-top:12px}
</style>
</head>
<body>

<header class="topbar">
  <div class="toplinks">Associate Psychologist Program &nbsp;/&nbsp; Blog &nbsp;/&nbsp; Satisfaction Guarantee</div>
  <div class="logo"><span class="dot"></span><div class="name">The Willow Lane<small>helping you create loving relationships</small></div></div>
  <a class="head-btn appoint">Request an Appointment</a>
  <a class="head-btn phone"><svg width="13" height="13" viewBox="0 0 24 24"><path fill="#1d8591" d="M6.6 10.8a15 15 0 006.6 6.6l2.2-2.2c.3-.3.7-.4 1-.2 1.1.4 2.3.6 3.6.6.6 0 1 .4 1 1V20c0 .6-.4 1-1 1A17 17 0 013 4c0-.6.4-1 1-1h3.5c.6 0 1 .4 1 1 0 1.3.2 2.5.6 3.6.1.3 0 .7-.2 1z"/></svg>1300 555 014</a>
</header>
<nav class="nav">
  <a class="active">Home</a><a>About Us</a><a>Counselling Types</a><a>Relationship Counselling Locations</a><a>Sex Therapy Locations</a><a>Quizzes</a><a>Fees &amp; Rebates</a><a>FAQs</a><a>Contact Us</a>
</nav>

<section class="hero" role="img" aria-label="Smiling couple embracing on a beach at sunset">
  <h1>Expert Relationship &amp;<br>Marriage Counselling</h1>
  <form class="search">
    <h3>Search our Therapists Near You</h3>
    <div class="field">Select Type of Counselling <span>⌄</span></div>
    <div class="row"><div class="field" style="width:152px">Location</div><span class="or">Or</span><div class="field" style="width:152px">Postcode</div></div>
    <span class="btn">Search</span>
  </form>
  <svg class="abs" style="left:0;bottom:0" width="1200" height="110" viewBox="0 0 1200 110"><path d="M0 80 C200 10 420 20 600 55 S1000 70 1200 30 V110 H0Z" fill="#1d8591" opacity=".85"/><path d="M0 95 C250 40 450 60 650 80 S1000 75 1200 45 V110 H0Z" fill="#fff"/></svg>
</section>

<section>
  <div class="about-text">
    <div class="eyebrow">The Willow Lane</div>
    <h2 class="section-title" style="margin-bottom:16px">About Us</h2>
    <p>Our vision is to be the most highly regarded and comprehensive marriage counselling, relationship counselling and sex therapy service in Australia, at reasonable and affordable rates.</p>
    <p>We have hand chosen our team of Registered Psychologists, Counsellors and Sex Therapists considering their knowledge, compassion, and unbiased approach to marriage counselling and sexual therapy and their experience in the relationship field.</p>
    <p>We also provide our team with in-house, relationship training and conferences with world renowned international guest speakers as we have a strong commitment to continually keeping up to date and improving our methods.</p>
    <a class="btn" style="margin-top:12px">Learn More</a>
  </div>
  <div class="ph about-img" role="img" aria-label="Group therapy session with people seated in a circle"></div>
</section>

<section>
  <div class="ph water spec-band"></div>
  <div class="spec-card">
    <div class="spec-img" role="img" aria-label="Portrait of a smiling counsellor"><a class="btn btn-red">Request an Appointment</a></div>
    <div class="spec-body">
      <div class="eyebrow">Consult Us</div>
      <h2 class="section-title" style="margin-bottom:18px">We Specialise in Relationship<br>&amp; Marriage Counselling</h2>
      <p>You've come to the right place if you value your relationship, (along with being true to yourself) and would like help with how to repair the inevitable difficulties that come up in most relationships, and build a stronger more authentic connection.</p>
      <p>None of us, when we fall in love, imagine how difficult our relationship is going to be at times. We always hope for the best, then do our best, and still we can find that we are stranded in problems that we don't really understand. We can unwittingly get into distressing lose-lose negative cycles, and not know how to get out of them.</p>
      <a class="btn">Learn More</a>
    </div>
  </div>
</section>

<section>
  <div class="center eyebrow" style="top:1628px;font-size:14px">What We Provide</div>
  <div class="center section-title" style="top:1656px">Areas of Specialty Are</div>
  <span class="arrow" style="left:80px">←</span><span class="arrow" style="left:1096px">→</span>
  <div class="areas-card" style="left:122px"><div class="ph" role="img" aria-label="Couple sitting apart on a sofa" style="background:linear-gradient(135deg,#eee,#b9b2a9)"></div><span class="badge"></span><h4>Relationship Counselling</h4><div class="q">Do you need help with:</div><div class="d">Communication, recovering from an affair, loss of intimacy and love or power battles?</div></div>
  <div class="areas-card" style="left:448px"><div class="ph" role="img" aria-label="Frustrated woman shouting in an office" style="background:linear-gradient(135deg,#a9b8aa,#56665a)"></div><span class="badge"></span><h4>Anger Management Counselling</h4><div class="q">Do you need help with:</div><div class="d">Managing irrational outbursts, while learning to express your anger in healthy ways?</div></div>
  <div class="areas-card" style="left:772px"><div class="ph" role="img" aria-label="Man and woman standing with arms crossed" style="background:linear-gradient(135deg,#f1f1ef,#c9c4ba)"></div><span class="badge"></span><h4>Narcissism Counselling</h4><div class="q">Do you need help with:</div><div class="d">Managing narcissistic, superior, entitled, arrogant behaviour or lack of empathy?</div></div>
</section>

<section>
  <div class="ph ther"></div>
  <div class="ph ther-img" role="img" aria-label="Couple embracing inside a heart-shaped frame"></div>
  <div class="ther-text">
    <div class="eyebrow" style="font-size:13px">Therapy Helps In</div>
    <h2>Our Relationship Therapists</h2>
    <div class="lead">Can help with the following common relationship<br>issues, and more:</div>
  </div>
  <ul class="ther-list" style="left:478px">
    <li><svg width="11" height="10" viewBox="0 0 24 22"><path fill="#fff" d="M12 21 2 11A6 6 0 0112 3a6 6 0 0110 8z"/></svg>Affairs</li>
    <li><svg width="11" height="10" viewBox="0 0 24 22"><path fill="#fff" d="M12 21 2 11A6 6 0 0112 3a6 6 0 0110 8z"/></svg>Controlling behaviour</li>
    <li><svg width="11" height="10" viewBox="0 0 24 22"><path fill="#fff" d="M12 21 2 11A6 6 0 0112 3a6 6 0 0110 8z"/></svg>Verbal abuse</li>
    <li><svg width="11" height="10" viewBox="0 0 24 22"><path fill="#fff" d="M12 21 2 11A6 6 0 0112 3a6 6 0 0110 8z"/></svg>Imbalance of power</li>
    <li><svg width="11" height="10" viewBox="0 0 24 22"><path fill="#fff" d="M12 21 2 11A6 6 0 0112 3a6 6 0 0110 8z"/></svg>Lack of intimacy</li>
    <li><svg width="11" height="10" viewBox="0 0 24 22"><path fill="#fff" d="M12 21 2 11A6 6 0 0112 3a6 6 0 0110 8z"/></svg>Poor communication</li>
    <li><svg width="11" height="10" viewBox="0 0 24 22"><path fill="#fff" d="M12 21 2 11A6 6 0 0112 3a6 6 0 0110 8z"/></svg>Loss of love</li>
  </ul>
  <ul class="ther-list" style="left:772px">
    <li><svg width="11" height="10" viewBox="0 0 24 22"><path fill="#fff" d="M12 21 2 11A6 6 0 0112 3a6 6 0 0110 8z"/></svg>Relationship neglect</li>
    <li><svg width="11" height="10" viewBox="0 0 24 22"><path fill="#fff" d="M12 21 2 11A6 6 0 0112 3a6 6 0 0110 8z"/></svg>Sexual problems</li>
    <li><svg width="11" height="10" viewBox="0 0 24 22"><path fill="#fff" d="M12 21 2 11A6 6 0 0112 3a6 6 0 0110 8z"/></svg>Problems from childhood</li>
    <li><svg width="11" height="10" viewBox="0 0 24 22"><path fill="#fff" d="M12 21 2 11A6 6 0 0112 3a6 6 0 0110 8z"/></svg>Problems with parenting your children</li>
    <li><svg width="11" height="10" viewBox="0 0 24 22"><path fill="#fff" d="M12 21 2 11A6 6 0 0112 3a6 6 0 0110 8z"/></svg>Step children and in-laws</li>
    <li><svg width="11" height="10" viewBox="0 0 24 22"><path fill="#fff" d="M12 21 2 11A6 6 0 0112 3a6 6 0 0110 8z"/></svg>All forms of family problems</li>
    <li><svg width="11" height="10" viewBox="0 0 24 22"><path fill="#fff" d="M12 21 2 11A6 6 0 0112 3a6 6 0 0110 8z"/></svg>Anger management problems</li>
  </ul>
</section>

<section>
  <div class="appr-text">
    <div class="eyebrow" style="font-size:14px">Therapy Helps In</div>
    <h2 class="section-title" style="margin-bottom:16px">Our Marriage Counselling<br>Approach</h2>
    <p>It is very important to us that we take a very positive approach to relationship counselling. From your very first session, we will take the time to fully understand each of your individual perspectives, without bias, and get to the very root of the issues that are affecting your relationship.</p>
    <p>Once we have a clear understanding of what's been going on, we will compassionately guide you and your partner beyond the dynamics that have been causing you problems.</p>
    <p>We will work with you and your partner to create a positive action plan, one that will help you make real progress towards rediscovering your happiness together.</p>
    <p>Although couples therapy is the quickest and most effective way to re-establish harmony in a relationship, it's important to remember that Rome wasn't built in a day. The process can be challenging and will generally require more than one or two sessions to achieve lasting results, but be rest assured that you will be making progress with each session and be starting to feel better.</p>
  </div>
  <div class="ph appr-img" role="img" aria-label="Couple talking with a therapist in a bright room"></div>
</section>

<section>
  <div class="ph loc-band" role="img" aria-label="Soft ocean waves over rocks"></div>
  <div class="loc">
    <h2 class="section-title sub-title">Our Marriage Counselling<br>Locations</h2>
    <p style="font-size:10px">We currently have marriage and relationship counselling services in:</p>
    <div class="loc-grid">
      <span><b>Melbourne</b> - 43 centres</span><span><b>Brisbane</b> - 22 centres</span><span><b>Sydney</b> - 26 centres</span>
      <span><b>Canberra</b> - 2 centres</span><span><b>Gold Coast</b> - 5 centres</span><span><b>Adelaide</b> - 6 centres</span>
      <span><b>Perth</b> - 12 centres</span><span><b>Sunshine Coast</b> - 2 centres</span><span><b>Wollongong</b> - 1 centre</span>
      <span><b>Wodonga</b> - 1 centre</span><span><b>Townsville</b> - 1 centre</span><span><b>Central Coast</b> - 3 centres</span>
    </div>
  </div>
  <div class="comm">
    <h2 class="section-title sub-title">Communication is a Vital Skill<br>but not Often Taught to Us</h2>
    <p style="font-size:10px">Many people find that their ways of communicating with each other hamper them from having a happy healthy relationship.</p>
    <p style="font-size:10px">Effective Interpersonal Communication skills are not something that most people are taught. But almost everyone has trouble expressing difficulties in their relationship, feels their partner fails to hear them, or cannot share their thoughts and feelings safely. We help couples learn these skills in supportive sessions.</p>
  </div>
</section>

<section>
  <div class="vbox" style="left:122px"><span class="icon"></span><h4>REBATES AVAILABLE</h4><p>You may be able to receive rebates of up to 75% of your session costs.</p><a class="btn">Learn More</a></div>
  <div class="vbox" style="left:448px"><span class="icon"></span><h4>SATISFACTION GUARANTEE</h4><p>We're proud to offer our 100% risk-free, satisfaction guarantee.</p><a class="btn">Learn More</a></div>
  <blockquote class="quote"><div><span class="marks">“</span><br><span class="big">Connection</span> is the energy that grows between people when they feel seen, heard and valued; when they can give and receive without judgment; and when they draw strength from the relationship.<br><span style="font-size:11px">– Clara Mendes</span><br><span class="marks" style="float:right">”</span></div></blockquote>
</section>

<section>
  <div class="ph tiles-band" role="img" aria-label="Misty shoreline backdrop"></div>
  <div class="tile" style="left:122px;background:linear-gradient(135deg,#e9ecee,#9aa3a8)" role="img" aria-label="Worried man sitting on a bed"><div class="cap">How To Deal With an Affair ?</div></div>
  <div class="tile" style="left:448px;background:linear-gradient(135deg,#a9a2a0,#5b5553)" role="img" aria-label="Two men resting heads together"><div class="cap">Same Sex Relationships</div></div>
  <div class="tile" style="left:772px;background:linear-gradient(135deg,#f2f2f0,#a7a7a5)" role="img" aria-label="Stressed woman on the phone"><div class="cap">Are You living with a narcissist?</div></div>
</section>

<section>
  <div class="ph news-band" role="img" aria-label="Misty forest backdrop"></div>
  <div class="center eyebrow" style="top:4138px;font-size:14px">Our Blogs</div>
  <div class="center section-title" style="top:4162px">News &amp; Articles</div>

  <article class="post" style="left:143px;top:4228px;height:276px"><span class="ph" style="height:176px;background:linear-gradient(135deg,#f0eeec,#c4bdb6)" role="img" aria-label="Pensive woman with hands on head"></span><div class="txt">What is Borderline Personality Disorder and how does it affect my relationship?<div class="date">▣ 24 June 2020</div></div></article>
  <article class="post" style="left:375px;top:4228px;height:276px"><div class="txt">Sexual Desires in Men and Women: What Are the Real Differences?<div class="date">▣ 05 May 2020</div></div><span class="ph" style="height:176px;background:linear-gradient(135deg,#d9cdc6,#8f7f77)" role="img" aria-label="Couple laughing in bed"></span></article>
  <article class="post" style="left:606px;top:4228px;height:276px"><span class="ph" style="height:176px;background:linear-gradient(135deg,#d4c6c0,#7d6c66)" role="img" aria-label="Couple lying together"></span><div class="txt">6 Steps To Becoming An Emotionally Available Lover<div class="date">▣ 20 April 2020</div></div></article>
  <article class="post" style="left:838px;top:4228px;height:276px"><div class="txt">Sexual Desires in Men and Women: What Are the Real Differences?<div class="date">▣ 05 May 2020</div></div><span class="ph" style="height:176px;background:linear-gradient(135deg,#f1f1f1,#b6a9b8 70%,#777)" role="img" aria-label="Person holding a megaphone to a partner"></span></article>

  <article class="post" style="left:143px;top:4516px;height:278px"><span class="ph" style="height:176px;background:linear-gradient(135deg,#4b4d52,#16181b)" role="img" aria-label="Person using a laptop in the dark"></span><div class="txt">How Normal Is It To Watch Porn?<span class="more">Read More »</span></div></article>
  <article class="post" style="left:375px;top:4516px;height:278px"><div class="txt">Letter for a Partner Doubtful About Relationship Counselling<span class="more">Read More »</span></div><span class="ph" style="height:176px;background:linear-gradient(135deg,#eceff1,#9ba6ad)" role="img" aria-label="Couple in a counselling session"></span></article>
  <article class="post" style="left:606px;top:4516px;height:278px"><span class="ph" style="height:176px;background:linear-gradient(135deg,#cfc4bc,#7a6c64)" role="img" aria-label="Busy professional in a hallway"></span><div class="txt">Is Your Pursuit of Success Sabotaging Your Relationships That Matter Most?<span class="more">Read More »</span></div></article>
  <article class="post" style="left:838px;top:4516px;height:278px"><div class="txt">Recovering from an affair<span class="more">Read More »</span></div><span class="ph" style="height:176px;background:linear-gradient(135deg,#e6ddd3,#8d7b6c)" role="img" aria-label="Couple sitting apart"></span></article>

  <div class="center" style="top:4862px"><a class="btn" style="padding:12px 30px">View All Posts</a></div>
</section>

<footer class="ph footer">
  <div class="abs" style="left:120px;top:76px">
    <div class="logo" style="position:static"><span class="dot" style="background:#fff"></span><div class="name" style="color:#fff">The Willow Lane<small style="color:#fff">helping you create loving relationships</small></div></div>
    <div class="social"><span></span><span></span><span></span><span></span></div>
  </div>
  <div class="abs" style="left:398px;top:62px">
    <h5>Menu</h5>
    <div style="display:flex;gap:40px">
      <ul><li>› Home</li><li>› About Us</li><li>› Our Blogs</li><li>› Members Log In</li><li>› Contact Us</li></ul>
      <ul><li>› Relationship Counselling</li><li>› Sex Therapy</li><li>› Fees and Rebates</li><li>› FAQ's</li></ul>
    </div>
  </div>
  <div class="abs" style="left:712px;top:62px"><h5>Quick Contact</h5></div>
  <div class="contact-item" style="left:712px;top:102px"><span class="ic"><svg width="12" height="12" viewBox="0 0 24 24"><path fill="#1d8591" d="M12 2a7 7 0 00-7 7c0 5 7 13 7 13s7-8 7-13a7 7 0 00-7-7zm0 9.5A2.5 2.5 0 1112 6a2.5 2.5 0 010 5.5z"/></svg></span><span>12 Riverbend Ave,<br>Ashgrove, New South Wales</span></div>
  <div class="contact-item" style="left:904px;top:102px"><span class="ic"><svg width="12" height="12" viewBox="0 0 24 24"><path fill="#1d8591" d="M6.6 10.8a15 15 0 006.6 6.6l2.2-2.2c.3-.3.7-.4 1-.2 1.1.4 2.3.6 3.6.6.6 0 1 .4 1 1V20c0 .6-.4 1-1 1A17 17 0 013 4c0-.6.4-1 1-1h3.5c.6 0 1 .4 1 1 0 1.3.2 2.5.6 3.6.1.3 0 .7-.2 1z"/></svg></span><span>123-555-0190</span></div>
  <div class="contact-item" style="left:712px;top:150px"><span class="ic"><svg width="12" height="12" viewBox="0 0 24 24"><rect x="6" y="2" width="12" height="20" rx="2" fill="#1d8591"/></svg></span><span style="font-size:12px;font-weight:600">1300 555 014</span></div>
  <div class="contact-item" style="left:904px;top:150px"><span class="ic"><svg width="12" height="12" viewBox="0 0 24 24"><path fill="#1d8591" d="M2 5h20v14H2zm2 2v.5l8 5 8-5V7z"/></svg></span><span style="text-decoration:underline">info@thewillowlane.com.au</span></div>
  <div class="copy">© 2020 THE WILLOW LANE. All rights reserved.</div>
</footer>

</body>
</html>
```